Business Card Design Project

We require a business card template to cover basic contact information - our company logo, names of employees, title, mobile and email.

Target Market(s)

Corporate

Industry/Entity Type

Business

Font styles to use
Sans Serif

Requirements
Nice to have
• Thinking it would be great just to have the logo taking up approximately half the space (so it goes as far across the top of the card as possible) and then contact details in the lower half of the card. Keen just to use only the two colours in the logo, on a white background.
Should not have
• No fussy drawings

```html
<!DOCTYPE html>
<html lang="en">
<head>
<meta charset="utf-8">
<title>Tidewell Developments – Business Card</title>
<link rel="stylesheet" href="https://fonts.googleapis.com/css2?family=Questrial&display=swap">
<style>
  :root {
    --backdrop: #e6e9ec;
    --card-white: #ffffff;
    --teal: #2fa4b7;
    --deep-blue: #2462ad;
    --text-light: #ffffff;
    --type: "Questrial", sans-serif;
  }
  * { box-sizing: border-box; margin: 0; padding: 0; }
  html, body {
    width: 1200px;
    height: 900px;
    overflow: hidden;
    background: var(--backdrop);
    font-family: var(--type);
  }
  .business-card {
    position: absolute;
    left: 104px;
    top: 144px;
    width: 993px;
    height: 613px;
    background: var(--card-white);
    overflow: hidden;
    box-shadow: 0 6px 24px rgba(0,0,0,0.12);
  }
  .brand {
    position: absolute;
    left: 0;
    top: 0;
    width: 100%;
    height: 363px;
    color: var(--teal);
    font-family: var(--type);
    font-weight: 400;
  }
  .brand-name {
    position: absolute;
    left: 53px;
    top: 40px;
    font-size: 218px;
    line-height: 1;
    letter-spacing: -4px;
  }
  .brand-descriptor {
    position: absolute;
    right: 72px;
    top: 282px;
    font-size: 50px;
    line-height: 1;
  }
  .divider-band {
    position: absolute;
    left: 0;
    top: 363px;
    width: 100%;
    height: 21px;
    background: var(--deep-blue);
  }
  .contact-panel {
    position: absolute;
    left: 0;
    top: 384px;
    width: 100%;
    height: 229px;
    background: var(--teal);
    color: var(--text-light);
  }
  .person-name {
    position: absolute;
    left: 61px;
    top: 12px;
    font-size: 30px;
    color: var(--deep-blue);
  }
  .person-title {
    position: absolute;
    left: 63px;
    top: 52px;
    font-size: 23px;
  }
  .contact-line {
    position: absolute;
    left: 58px;
    display: flex;
    align-items: center;
    gap: 8px;
    font-size: 31px;
  }
  .contact-line svg { flex: none; }
  .contact-phone { top: 91px; }
  .contact-email { top: 133px; }
</style>
</head>
<body>
  <section class="business-card">
    <header class="brand" aria-label="Tidewell developments">
      <div class="brand-name">Tidewell</div>
      <div class="brand-descriptor">developments</div>
    </header>

    <div class="divider-band"></div>

    <div class="contact-panel">
      <p class="person-name">Nina Calder</p>
      <p class="person-title">Manager</p>

      <p class="contact-line contact-phone">
        <svg width="38" height="38" viewBox="0 0 24 24" aria-hidden="true">
          <path fill="#2462ad" d="M6.6 2.5c.6-.3 1.3-.1 1.6.5l1.7 3.2c.3.6.2 1.2-.3 1.6L8.2 8.9c.9 2.4 2.7 4.5 5 5.9l1.3-1.2c.5-.4 1.1-.5 1.6-.2l3.2 1.8c.6.3.8 1 .5 1.6l-1 2c-.5.9-1.5 1.4-2.5 1.2C9.7 18.7 4.8 13.3 3.6 6.8c-.2-1 .3-2 1.2-2.5z"/>
        </svg>
        <span>0400 555 018</span>
      </p>

      <p class="contact-line contact-email">
        <svg width="46" height="34" viewBox="0 0 46 34" aria-hidden="true">
          <rect x="1" y="4" width="44" height="29" rx="2" fill="#2462ad"/>
          <path d="M2 6 L23 21 L44 6" fill="none" stroke="#2fa4b7" stroke-width="2"/>
          <path d="M2 32 L17 17 M44 32 L29 17" fill="none" stroke="#2fa4b7" stroke-width="1.5"/>
          <rect x="15" y="1" width="16" height="13" fill="#ffffff" opacity="0.9"/>
          <path d="M18 5h10M18 8h10M18 11h7" stroke="#2462ad" stroke-width="1.3"/>
        </svg>
        <span>nina.calder@example.com</span>
      </p>
    </div>
  </section>
</body>
</html>
```